Professional, Attractive, Simple Website Needed!!

We completed the design for our logo.

We need a website built out around this.

Here are a couple samples of how we want ours formatted.

http://brvntapower.com

http://www.halvorbeam.com/lp/free-quote?LeadSource=Search%20Engine&ProgramName=webquery&experience=qual&language=en&type=brd&gclid=Xq7RTPwmEYKDLAvUHbsNQkfPZrTcGwnJuoVbXeLqHmRYdAsWtPkMcNfBYgzTrUoQJhEdWvKpYaLsZbCmNDgQwTxAoKpXbT_qkR

http://morvalo.co

Reason: Extending this deadline due to our delay in providing designers with content for each page. This is coming in next 24 hours.

Reason: Due to scheduling conflicts and extended travel delays related to Puerto Rico, the deadline has been extended. Your patience is greatly appreciated.

Reason: Travel and scheduling conflicts have made it impossible to give this project the thorough review it deserves, therefore I am extending the deadline. Thank you for your patience!

Target Market(s)

Home Owners who earn 60k + household annually

Industry/Entity Type

It Professional

Coding

Coded - Design and coding required

Number of Pages Required

5+ page

Font styles to use
Serif

Colors
34a7d8
9bcb3c

Requirements
Must have
• Simple
• Lead form Entry (Ability for visitor to enter Name, number and address for a quote)
• Sleek Design
• Professional
• Testimonials
• Use color Scheme of Design Logo Attached
Nice to have
• Video when site starts
• Like this
• https://www.vidmarrow.com/watch?v=qT8mRpXw2Ka&feature=vidm.ro
Should not have
• Should not include Commercial solar
• Should not include wind power

```html
<!DOCTYPE html>
<html lang="en">
<head>
<meta charset="utf-8">
<title>Brightfield Energy – Home Solar</title>
<link href="https://fonts.googleapis.com/css2?family=Jost:wght@400;500&display=swap" rel="stylesheet">
<style>
:root{
  --blue:#34a7d8;
  --green:#9bcb3c;
  --navy:#0b2239;
  --ink:#1d2a3a;
  --text:#4a4f57;
  --muted:#9aa0a6;
  --line:#e6e8ea;
  --paper:#f3f3f2;
  --white:#ffffff;
}
*{box-sizing:border-box;margin:0;padding:0}
html,body{width:1200px;height:2338px;overflow:hidden}
body{position:relative;font-family:'Jost',sans-serif;color:var(--text);background:var(--white)}
a{color:inherit;text-decoration:none}
.abs{position:absolute}

/* header */
.site-header{position:absolute;left:0;top:0;width:1200px;height:97px;background:rgba(40,40,40,.55);z-index:5}
.brand{position:absolute;left:156px;top:28px;font-size:20px;font-weight:500;color:var(--blue);letter-spacing:.5px}
.brand-dot{display:inline-block;width:14px;height:14px;border-radius:50%;background:var(--green);margin-right:8px;vertical-align:-1px}
.main-nav{position:absolute;left:329px;top:64px;width:715px;display:flex;justify-content:space-between;font-size:13px;color:var(--white)}
.main-nav a.active{color:var(--green)}
.call-top{position:absolute;left:737px;top:22px;font-size:14px;color:var(--white);display:flex;align-items:center;gap:8px}
.call-top .label{color:var(--blue)}
.btn{display:inline-block;text-transform:uppercase;font-size:11px;letter-spacing:1px;color:var(--white);text-align:center}
.btn-green{background:var(--green)}
.btn-blue{background:var(--blue)}
.get-started{position:absolute;left:916px;top:15px;width:128px;height:32px;line-height:32px}

/* hero */
.hero{position:absolute;left:0;top:0;width:1200px;height:553px;background:linear-gradient(180deg,#8d9497 0%,#6f7a80 25%,#49555c 45%,#4b6a35 75%,#3f6a2a 100%)}
.hero-copy{position:absolute;left:156px;top:238px;color:var(--white)}
.hero-copy h1{font-size:23px;font-weight:500;line-height:30px}
.hero-copy h1 .blue{color:var(--blue)}
.hero-copy h1 .green{color:var(--green)}
.hero-copy p{font-size:15px;line-height:20px;margin-top:14px}
.play{position:absolute;left:155px;top:505px;width:97px;height:80px;background:var(--white);box-shadow:0 2px 6px rgba(0,0,0,.15)}
.play-top{height:48px;background:var(--blue);display:flex;align-items:center;justify-content:center}
.play span{display:block;text-align:center;font-size:11px;letter-spacing:1px;color:var(--ink);margin-top:10px}

/* quote form */
.form-accent{position:absolute;left:728px;top:174px;width:227px;height:270px;background:var(--green)}
.quote-card{position:absolute;left:752px;top:198px;width:280px;height:388px;background:var(--white);box-shadow:0 6px 14px rgba(0,0,0,.2)}
.quote-card h2{text-align:center;font-size:23px;font-weight:400;color:var(--blue);margin-top:24px}
.quote-card h2 .green{color:var(--green)}
.quote-card .sub{text-align:center;font-size:16px;color:var(--text);margin-top:2px}
.fields{margin-top:18px;border-bottom:1px solid var(--line)}
.field{height:49px;border-top:1px solid var(--line);display:flex;align-items:center;padding-left:28px;font-size:12px;color:var(--muted);gap:12px}
.form-foot{position:absolute;left:0;bottom:36px;width:280px;display:flex;align-items:center}
.form-foot .tel{margin-left:24px;font-size:14px;color:var(--text);display:flex;align-items:center;gap:8px}
.quote-btn{position:absolute;left:156px;top:-16px;width:134px;height:32px;line-height:32px}

/* about */
.about{position:absolute;left:0;top:553px;width:1200px;height:525px;overflow:hidden}
.roof{position:absolute;left:0;top:230px;width:1200px;height:295px;background:linear-gradient(180deg,rgba(255,255,255,1) 0%,rgba(214,231,245,.9) 22%,#c96a4b 45%,#3c5a86 62%,#b3553a 85%,#a0452f 100%)}
.about-mark{position:absolute;left:576px;top:72px;width:48px;height:48px;border-radius:50%;border:3px solid var(--green)}
.section-title{display:flex;align-items:center;justify-content:center;gap:20px;font-weight:400}
.about h2{position:absolute;top:118px;left:0;width:1200px;font-size:28px;color:var(--blue)}
.about h2 .green{color:var(--green)}
.about h2 .rule{display:block;width:48px;height:2px;background:var(--blue)}
.about h2 .rule.g{background:var(--green)}
.about p{position:absolute;left:255px;top:175px;width:690px;text-align:center;font-size:14px;line-height:19px;color:var(--text)}
.learn{position:absolute;left:536px;top:266px;width:128px;height:32px;line-height:32px}

/* features */
.features{position:absolute;left:0;top:1078px;width:1200px;height:464px;background:var(--paper)}
.features h2,.savings h2{font-size:27px;font-weight:400;color:var(--ink)}
.features h2{position:absolute;top:62px;left:0;width:1200px}
.rule-dark{display:block;width:50px;height:2px;background:var(--ink)}
.feature{position:absolute;top:121px;width:240px;text-align:center}
.photo-ring{width:158px;height:158px;border-radius:50%;margin:0 auto;border:6px solid #dcdcdc}
.feature h3{font-size:18px;font-weight:400;color:var(--ink);margin-top:24px}
.feature p{font-size:13px;line-height:17px;margin-top:8px;color:var(--text)}
.feature a{display:inline-block;font-size:11px;color:var(--blue);text-decoration:underline;margin-top:22px;letter-spacing:.5px}
.feature a.hot{color:var(--green)}

/* savings */
.savings{position:absolute;left:0;top:1542px;width:1200px;height:448px;background:var(--white)}
.savings h2{position:absolute;left:156px;top:56px;display:flex;align-items:center;gap:20px}
.savings h2 .rule-dark{width:48px}
.view-all{position:absolute;left:932px;top:62px;width:111px;height:32px;line-height:32px}
.testimonial{position:absolute;top:128px;width:316px}
.testimonial.t2{width:282px}
.avatar{width:152px;height:152px;border-radius:50%;border:1px solid var(--line);padding:14px}
.avatar div{width:100%;height:100%;border-radius:50%}
.who{font-size:14px;color:var(--ink);margin-top:12px}
.who .place{color:var(--muted)}
.quote{font-size:12px;line-height:18px;margin-top:12px;color:var(--text)}
.stars{display:flex;gap:3px;margin-top:16px}
.t2 .who,.t2 .quote{color:var(--blue)}
.arrow{position:absolute;top:250px}

/* footer */
.site-footer{position:absolute;left:0;top:1990px;width:1200px;height:348px;background:var(--navy);color:var(--white)}
.foot-mark{position:absolute;left:572px;top:66px;width:56px;height:56px;border-radius:50%;border:3px solid var(--green)}
.foot-brand{position:absolute;left:0;top:130px;width:1200px;text-align:center;font-size:20px;font-weight:500;color:var(--blue)}
.foot-addr{position:absolute;left:156px;top:138px;font-size:13px;line-height:18px}
.foot-contact{position:absolute;right:156px;top:138px;font-size:13px;line-height:18px;text-align:right}
.foot-contact .g{color:var(--green)}
.foot-nav{position:absolute;left:243px;top:210px;width:715px;display:flex;justify-content:space-between;font-size:13px}
.foot-nav a.active{color:var(--green)}
.foot-rule{position:absolute;left:0;top:270px;width:1200px;height:1px;background:#1f3850}
.copy{position:absolute;left:156px;top:302px;font-size:12px}
.copy .blue{color:var(--blue)}
.social{position:absolute;left:857px;top:294px;display:flex;gap:8px}
.social span{width:28px;height:28px;border:1px solid var(--green)}
.social span.on{background:var(--green)}
.to-top{position:absolute;left:1014px;top:294px;width:28px;height:28px;border-radius:50%;background:var(--blue);display:flex;align-items:center;justify-content:center}
</style>
</head>
<body>

<section class="hero" role="img" aria-label="Photo of rows of ground-mounted solar panels on a grassy field under a grey sky"></section>

<header class="site-header">
  <a class="brand" href="#"><span class="brand-dot"></span>Brightfield Energy</a>
  <div class="call-top"><span class="label">Call Us:</span>
    <svg width="18" height="18" viewBox="0 0 24 24" fill="none" stroke="#34a7d8" stroke-width="2"><path d="M5 3h4l2 5-3 2a12 12 0 0 0 6 6l2-3 5 2v4a2 2 0 0 1-2 2A17 17 0 0 1 3 5a2 2 0 0 1 2-2z"/></svg>
    <span>123-456-7890</span></div>
  <a class="btn btn-green get-started" href="#">Get Started</a>
  <nav class="main-nav">
    <a class="active" href="#">-- Home -</a><a href="#">About us</a><a href="#">Why BFE</a><a href="#">How It Works</a><a href="#">Testimonials</a><a href="#">Blog</a><a href="#">Contact Us</a>
  </nav>
</header>

<div class="hero-copy">
  <h1>Save <span class="blue">$$$</span> by using Best available Energy<br>Source - <span class="green">Solar Energy!</span></h1>
  <p>Already in process to Help our clients to save aroung<br>20% - 30%* on their Power Bills.</p>
</div>

<a class="play" href="#">
  <div class="play-top"><svg width="30" height="30" viewBox="0 0 30 30" fill="none" stroke="#fff" stroke-width="2"><circle cx="15" cy="15" r="13"/><path d="M12 9.5v11l8.5-5.5z"/></svg></div>
  <span>PLAY VIDEO</span>
</a>

<div class="form-accent"></div>
<form class="quote-card">
  <h2>Brightfield <span class="green">Energy</span></h2>
  <div class="sub">inquire now!</div>
  <div class="fields">
    <div class="field"><svg width="11" height="11" viewBox="0 0 12 12" fill="#c4c8cc"><circle cx="6" cy="3.5" r="3"/><path d="M0 12a6 5 0 0 1 12 0z"/></svg>Name</div>
    <div class="field"><svg width="11" height="11" viewBox="0 0 12 12" fill="#c4c8cc"><rect x="0" y="2" width="12" height="9"/></svg>Email</div>
    <div class="field"><svg width="11" height="11" viewBox="0 0 24 24" fill="#c4c8cc"><path d="M5 3h4l2 5-3 2a12 12 0 0 0 6 6l2-3 5 2v4a2 2 0 0 1-2 2A17 17 0 0 1 3 5a2 2 0 0 1 2-2z"/></svg>Phone</div>
    <div class="field"><svg width="11" height="12" viewBox="0 0 12 14" fill="#c4c8cc"><path d="M6 0a5 5 0 0 1 5 5c0 4-5 9-5 9S1 9 1 5a5 5 0 0 1 5-5z"/></svg>Address</div>
  </div>
  <div class="form-foot">
    <div class="tel"><svg width="18" height="18" viewBox="0 0 24 24" fill="none" stroke="#34a7d8" stroke-width="2"><path d="M5 3h4l2 5-3 2a12 12 0 0 0 6 6l2-3 5 2v4a2 2 0 0 1-2 2A17 17 0 0 1 3 5a2 2 0 0 1 2-2z"/></svg>123-456-7890</div>
    <a class="btn btn-blue quote-btn" href="#">Get a Quote</a>
  </div>
</form>

<section class="about">
  <div class="roof" role="img" aria-label="Photo of a red tiled house roof with solar panels and white chimneys under a blue sky"></div>
  <div class="about-mark"></div>
  <h2 class="section-title"><span class="rule"></span><span>Brightfield <span class="green">Energy</span></span><span class="rule g"></span></h2>
  <p>Contrary to popular belief, Lorem Ipsum is not simply random text. It has roots in a piece of classical Latin literature from 45 BC, making it over 2000 years old. Edwin Harrowgate, a Latin professor at Ashcombe College in Vermont...</p>
  <a class="btn btn-green learn" href="#">Learn More</a>
</section>

<section class="features">
  <h2 class="section-title"><span class="rule-dark"></span>Sun Energy - The Best Resource<span class="rule-dark"></span></h2>
  <div class="feature" style="left:176px">
    <div class="photo-ring" style="background:linear-gradient(135deg,#b9c7d6,#d7b7a2 50%,#8c9aa8)" role="img" aria-label="Photo of a smiling couple"></div>
    <h3>Zero Cost</h3>
    <p>It is a long established fact that a<br>reader will be distracted.</p>
    <a href="#">GET STARTED</a>
  </div>
  <div class="feature" style="left:480px">
    <div class="photo-ring" style="background:linear-gradient(180deg,#5d86c4,#3a4a6a 50%,#5c8d3c)" role="img" aria-label="Photo of a house with solar panels on its roof"></div>
    <h3>Lower Energy Bills</h3>
    <p>It is a long established fact that a<br>reader will be distracted.</p>
    <a class="hot" href="#">GET STARTED</a>
  </div>
  <div class="feature" style="left:784px">
    <div class="photo-ring" style="background:linear-gradient(160deg,#4a9ee0,#e46a2a 45%,#2f4f86)" role="img" aria-label="Photo of a worker installing solar panels on a roof"></div>
    <h3>No Maintenance</h3>
    <p>It is a long established fact that a<br>reader will be distracted.</p>
    <a href="#">GET STARTED</a>
  </div>
</section>

<section class="savings">
  <h2><span class="rule-dark"></span>Already Saving on Power Bills</h2>
  <a class="btn btn-blue view-all" href="#">View All</a>
  <svg class="arrow" style="left:156px" width="22" height="40" viewBox="0 0 22 40" fill="none" stroke="#b8bcc0" stroke-width="2"><path d="M20 2L3 20l17 18"/></svg>
  <svg class="arrow" style="left:1022px" width="22" height="40" viewBox="0 0 22 40" fill="none" stroke="#9bcb3c" stroke-width="2"><path d="M2 2l17 18L2 38"/></svg>
  <article class="testimonial" style="left:232px">
    <div class="avatar"><div style="background:linear-gradient(180deg,#c9b9a0,#4a3b32)" role="img" aria-label="Photo of a happy family outside their home"></div></div>
    <div class="who">Marella P. <span class="place">/ Linwood, MA</span></div>
    <p class="quote">Contrary to popular belief, Lorem Ipsum is not simply random text. It has roots in a piece of classical Latin literature from 45 BC, making it over...</p>
    <div class="stars">
      <svg width="78" height="14" viewBox="0 0 78 14"><g fill="#9bcb3c"><path id="s" d="M7 0l2 4.5 5 .5-3.8 3.3 1.2 5L7 10.8 2.6 13.3l1.2-5L0 5l5-.5z"/><use href="#s" x="16"/><use href="#s" x="32"/></g><path d="M55 0l2 4.5 5 .5-3.8 3.3 1.2 5L55 10.8z" fill="#9bcb3c"/><g fill="none" stroke="#9bcb3c"><path d="M55 0l2 4.5 5 .5-3.8 3.3 1.2 5L55 10.8 50.6 13.3l1.2-5L48 5l5-.5z"/><path d="M71 .8l1.8 4.1 4.6.5-3.5 3 1.1 4.6L71 10.8l-4 2.2 1.1-4.6-3.5-3 4.6-.5z"/></g></svg>
    </div>
  </article>
  <article class="testimonial t2" style="left:664px">
    <div class="avatar"><div style="background:linear-gradient(180deg,#9aa9b8,#2c2f3a 60%,#b9324a)" role="img" aria-label="Photo of a smiling couple standing outdoors"></div></div>
    <div class="who">Doriane F. / Brookvale, MA</div>
    <p class="quote">Contrary to popular belief, Lorem Ipsum is not simply random text. It has roots in a piece of classical Latin literature from 45 BC, making it over...</p>
    <div class="stars">
      <svg width="78" height="14" viewBox="0 0 78 14"><g fill="#34a7d8"><path id="b" d="M7 0l2 4.5 5 .5-3.8 3.3 1.2 5L7 10.8 2.6 13.3l1.2-5L0 5l5-.5z"/><use href="#b" x="16"/><use href="#b" x="32"/></g><path d="M55 0l2 4.5 5 .5-3.8 3.3 1.2 5L55 10.8z" fill="#34a7d8"/><g fill="none" stroke="#34a7d8"><path d="M55 0l2 4.5 5 .5-3.8 3.3 1.2 5L55 10.8 50.6 13.3l1.2-5L48 5l5-.5z"/><path d="M71 .8l1.8 4.1 4.6.5-3.5 3 1.1 4.6L71 10.8l-4 2.2 1.1-4.6-3.5-3 4.6-.5z"/></g></svg>
    </div>
  </article>
</section>

<footer class="site-footer">
  <svg class="abs" style="left:156px;top:82px" width="22" height="32" viewBox="0 0 22 32" fill="none" stroke="#9bcb3c" stroke-width="2"><path d="M11 1a10 10 0 0 1 10 10c0 8-10 20-10 20S1 19 1 11A10 10 0 0 1 11 1z"/><circle cx="11" cy="11" r="4"/></svg>
  <svg class="abs" style="left:1014px;top:84px" width="30" height="30" viewBox="0 0 24 24" fill="none" stroke="#9bcb3c" stroke-width="1.6"><path d="M5 3h4l2 5-3 2a12 12 0 0 0 6 6l2-3 5 2v4a2 2 0 0 1-2 2A17 17 0 0 1 3 5a2 2 0 0 1 2-2z"/><path d="M15 3a6 6 0 0 1 6 6M15 7a2 2 0 0 1 2 2"/></svg>
  <div class="foot-mark"></div>
  <div class="foot-brand">Brightfield Energy</div>
  <div class="foot-addr">4450 Larkspur Meadow Blvd Fenwick,<br>NQ 60214</div>
  <div class="foot-contact"><span class="g">Call Us:</span> 123-456-7890<br><span class="g">Email:</span> info@brightfieldenergy.com</div>
  <nav class="foot-nav">
    <a class="active" href="#">-- Home -</a><a href="#">About us</a><a href="#">Why BFE</a><a href="#">How It Works</a><a href="#">Testimonials</a><a href="#">Blog</a><a href="#">Contact Us</a>
  </nav>
  <div class="foot-rule"></div>
  <div class="copy">© 2017 <span class="blue">Brightfield Energy</span>. All Rights Reserved.</div>
  <div class="social"><span></span><span class="on"></span><span></span><span></span></div>
  <a class="to-top" href="#"><svg width="12" height="12" viewBox="0 0 12 12" fill="none" stroke="#fff" stroke-width="2"><path d="M6 11V2M2 6l4-4 4 4"/></svg></a>
</footer>

</body>
</html>
```